Restyle corporate identity (+ logo) for a road construction company

We need a new logo and stationary design for our company VORMAX path. VORMAX path® increases the road base strength, while reducing major costs and time of road construction. Attached some examples of the current design.

Our wishes for the new logo:
- Business look
- Style sheet
- Modern

More information: www.vormaxpath-example.com
Updates

Target Market(s)

Government

Industry/Entity Type

Construction

Requirements
Must have
• Logo (with road sign) + text

```html
<!DOCTYPE html>
<html lang="en">
<head>
<meta charset="utf-8">
<title>VORMAX path – Stationery</title>
<link rel="stylesheet" href="https://fonts.googleapis.com/css2?family=Open+Sans:wght@400;600;700&display=swap">
<style>
  :root{
    --green:#9dc33c;
    --green-pale:#e2ecd0;
    --grey:#a3a4a6;
    --grey-dark:#5f6062;
    --paper:#ffffff;
    --paper-soft:#f3f3f3;
    --ground:#e4e4e4;
  }
  *{margin:0;padding:0;box-sizing:border-box}
  html,body{width:1200px;height:1048px;overflow:hidden}
  body{background:var(--ground);font-family:"Open Sans",Arial,sans-serif;color:var(--grey-dark);position:relative}

  .sheet{position:absolute;overflow:hidden;box-shadow:0 4px 14px rgba(0,0,0,.18)}
  .shape{position:absolute}

  .wordmark{position:absolute;display:flex;align-items:center;gap:8px;font-weight:700;color:var(--grey-dark);white-space:nowrap;letter-spacing:.5px}
  .wordmark .mark{background:var(--green);display:block}

  .contact{position:absolute;font-size:11px;line-height:1.45;font-weight:600;white-space:nowrap}
  .contact .label{color:var(--green);display:inline-block;width:44px}
  .contact.on-green{color:#fff}
  .contact.on-green .label{color:#fff}

  .web{position:absolute;color:#fff;font-weight:600;font-size:12px;white-space:nowrap}

  /* Letterhead */
  .letterhead{left:40px;top:40px;width:500px;height:707px;background:var(--paper)}
  .letterhead .wordmark{left:50px;top:60px;font-size:26px}
  .letterhead .wordmark .mark{width:14px;height:14px}
  .letterhead .top-grey{left:285px;top:118px;width:215px;height:16px;background:var(--grey);clip-path:polygon(0 0,100% 0,100% 100%,5% 100%)}
  .letterhead .top-green{left:290px;top:134px;width:210px;height:116px;background:var(--green);clip-path:polygon(0 0,100% 0,100% 100%,9% 100%)}
  .letterhead .top-green .contact{left:26px;top:16px;font-size:9px;line-height:1.6}
  .letterhead .top-green .contact .label{width:34px}
  .letterhead .foot-green{left:0;bottom:40px;width:300px;height:46px;background:var(--green);clip-path:polygon(0 0,100% 0,94% 100%,0 100%)}
  .letterhead .foot-grey{left:284px;bottom:0;width:216px;height:86px;background:var(--grey);clip-path:polygon(6% 0,100% 0,100% 100%,0 100%)}
  .letterhead .foot-grey .web{left:30px;top:46px}

  /* Envelope */
  .envelope{left:580px;top:40px;width:580px;height:276px;background:var(--paper-soft)}
  .envelope .top-grey{left:0;top:0;width:330px;height:16px;background:var(--grey);clip-path:polygon(0 0,100% 0,97% 100%,0 100%)}
  .envelope .side-green{left:335px;top:0;width:245px;height:150px;background:var(--green);clip-path:polygon(0 0,100% 0,100% 100%,12% 74%)}
  .envelope .wordmark{left:40px;top:36px;font-size:28px}
  .envelope .wordmark .mark{width:15px;height:15px}
  .envelope .contact{left:40px;top:108px}
  .envelope .foot-green{left:0;bottom:40px;width:330px;height:40px;background:var(--green);clip-path:polygon(0 0,100% 0,96% 100%,0 100%)}
  .envelope .foot-grey{left:318px;bottom:0;width:262px;height:80px;background:var(--grey);clip-path:polygon(5% 0,100% 0,100% 100%,0 100%)}
  .envelope .foot-grey .web{left:30px;top:46px}

  /* Business cards */
  .card{width:280px;height:160px;background:var(--paper);top:356px}
  .card-front{left:580px}
  .card-back{left:880px}
  .card .wordmark{font-size:19px}
  .card .wordmark .mark{width:10px;height:10px}
  .card-front .corner{left:0;top:0;width:70px;height:50px;background:var(--green-pale);clip-path:polygon(0 0,100% 0,0 100%)}
  .card-front .wordmark{left:118px;top:62px}
  .card-front .band-green{left:0;bottom:20px;width:150px;height:24px;background:var(--green);clip-path:polygon(0 0,100% 0,94% 100%,0 100%)}
  .card-front .band-green .web{left:12px;top:5px;font-size:8.5px;font-weight:400}
  .card-front .band-grey{left:142px;bottom:0;width:138px;height:44px;background:var(--grey);clip-path:polygon(6% 0,100% 0,100% 100%,0 100%)}
  .card-back .wordmark{left:18px;top:24px}
  .card-back .corner{right:0;top:70px;width:62px;height:90px;background:var(--green-pale);clip-path:polygon(100% 0,100% 100%,0 100%)}
  .card-back .band-green{left:0;bottom:22px;width:160px;height:56px;background:var(--green);clip-path:polygon(0 0,100% 0,94% 100%,0 100%)}
  .card-back .band-green ul{list-style:none;position:absolute;left:12px;top:6px;color:#fff;font-size:7.5px;line-height:1.6;white-space:nowrap}
  .card-back .band-green li::before{content:"";display:inline-block;width:5px;height:5px;background:#fff;margin-right:5px;vertical-align:middle}
  .card-back .band-grey{left:150px;bottom:0;width:130px;height:46px;background:var(--grey);clip-path:polygon(8% 0,100% 0,100% 100%,0 100%)}
  .card-back .person{position:absolute;right:20px;top:6px;text-align:right;color:#fff;line-height:1.3;white-space:nowrap}
  .card-back .person .name{font-size:9px;font-weight:700;color:var(--grey-dark)}
  .card-back .person .role{font-size:6.5px}
  .card-back .person .addr{font-size:6.5px}
  .card-back .person-icon{position:absolute;right:6px;top:8px;width:11px;height:11px;background:var(--green)}

  /* Logo display */
  .logo-display{position:absolute;left:580px;top:580px;width:580px;height:400px;display:flex;align-items:center;justify-content:center}
  .logo-display .wordmark{position:static;font-size:64px;gap:18px}
  .logo-display .wordmark .mark{width:34px;height:34px}
</style>
</head>
<body>

<section class="sheet letterhead" aria-label="Letterhead">
  <div class="shape top-grey"></div>
  <div class="shape top-green">
    <div class="contact on-green">
      Address Line 1, Address Line2,<br>Address Line 3<br>
      <span class="label">Email -</span>your mail@mailbox-example.com<br>
      <span class="label">Tel. -</span>+123 456 780<br>
      <span class="label">Fax. -</span>+123 456 789
    </div>
  </div>
  <div class="wordmark"><span class="mark"></span>VORMAX path</div>
  <div class="shape foot-green"></div>
  <div class="shape foot-grey"><span class="web">www.vormaxpath-example.com</span></div>
</section>

<section class="sheet envelope" aria-label="Envelope">
  <div class="shape top-grey"></div>
  <div class="shape side-green"></div>
  <div class="wordmark"><span class="mark"></span>VORMAX path</div>
  <div class="contact">
    Address Line 1, Address Line2,<br>Address Line 3<br>
    <span class="label">Email -</span>your mail@mailbox-example.com<br>
    <span class="label">Tel. -</span>+123 456 780<br>
    <span class="label">Fax. -</span>+123 456 789
  </div>
  <div class="shape foot-green"></div>
  <div class="shape foot-grey"><span class="web">www.vormaxpath-example.com</span></div>
</section>

<section class="sheet card card-front" aria-label="Business card front">
  <div class="shape corner"></div>
  <div class="wordmark"><span class="mark"></span>VORMAX path</div>
  <div class="shape band-green"><span class="web">www.vormaxpath-example.com</span></div>
  <div class="shape band-grey"></div>
</section>

<section class="sheet card card-back" aria-label="Business card back">
  <div class="shape corner"></div>
  <div class="wordmark"><span class="mark"></span>VORMAX path</div>
  <div class="shape band-green">
    <ul>
      <li>+123 456 780</li>
      <li>+123 456 789</li>
      <li>yourmail@mailbox-example.com</li>
      <li>www.vormaxpath-example.com</li>
    </ul>
  </div>
  <div class="shape band-grey">
    <div class="person">
      <div class="name">YOUR NAME</div>
      <div class="role">Position</div>
      <div class="addr">Address Line 1<br>Address Line 2, Address Line 3</div>
    </div>
    <span class="person-icon"></span>
  </div>
</section>

<section class="logo-display" aria-label="Logo">
  <div class="wordmark"><span class="mark"></span>VORMAX path</div>
</section>

</body>
</html>
```